Northgate Signal Shield LLC

Need help designing a web page for an alarm company. I want to promote my business.

Target Market(s)

Residential and commercial clients

Industry/Entity Type

Security Service

Coding

Coded - Design and coding required

Number of Pages Required

2 page

Font styles to use
Sans Serif

Requirements
Must have
• I would llike my logo displayed on the page. I would like my slogan displayed as well
´´A GREAT PLACE FOR YOUR SECURITY NEEDS´´
We are licensed and insured
Company phone number 713-555-0142
Company hours: Monday-Friday 8am-5pm Company address: P.O. Box 419 Crosby, TX 77064 over 25 years experience
Email info. Northgatess@ferntopmail.com
Company license #K52948316
Fire license# TMV-6614027
JLP-8170326
We offer alarm monitoring,security cameras, access control,gate openers, home theater systems, covert camera installations, FIre alarm installation and monitoring
Nice to have
• We offer security at competitive prices.
Get customer information for a free quote similar to brx website.
Should not have
• No prices listed on website

```html
<!DOCTYPE html>
<html lang="en">
<head>
<meta charset="utf-8">
<title>Northgate Signal Shield LLC – Security Services</title>
<link rel="stylesheet" href="https://fonts.googleapis.com/css2?family=Montserrat:wght@500;600;700;800;900&family=Open+Sans:wght@400;600;700&display=swap">
<style>
:root{
  --red:#e4202a;
  --red-dark:#b8121b;
  --ink:#1d1d1f;
  --text:#555a60;
  --muted:#8a8f96;
  --light:#f3f3f4;
  --line:#d9d9dc;
  --white:#ffffff;
  --night1:#1b2a6b;
  --night2:#3a2f7a;
  --night3:#0d1638;
  --orange:#f07a1a;
  --footer:#0f0f10;
}
*{box-sizing:border-box;margin:0;padding:0}
html,body{width:1200px;height:4000px;overflow:hidden}
body{font-family:"Open Sans",Arial,sans-serif;color:var(--text);background:var(--white);font-size:13px;line-height:1.6}
h1,h2,h3,h4,.nav,.btn{font-family:"Montserrat",Arial,sans-serif}
.wrap{width:760px;margin:0 auto;position:relative}
.btn{display:inline-block;background:var(--red);color:var(--white);font-weight:700;font-size:11px;letter-spacing:.5px;padding:10px 20px;text-transform:uppercase}
.btn-dark{background:var(--ink)}
.section-title{display:flex;align-items:center;justify-content:center;gap:18px;font-size:24px;font-weight:800;color:var(--ink);letter-spacing:1px;text-transform:uppercase}
.section-title::before,.section-title::after{content:"";width:60px;height:2px;background:var(--ink)}
.section-title.light{color:var(--white)}
.section-title.light::before,.section-title.light::after{background:var(--white)}
.ph{display:block}

/* header */
.site-header{height:140px;background:var(--white)}
.site-header .wrap{height:140px;display:flex;align-items:center;justify-content:space-between}
.brand{display:flex;align-items:center;gap:10px;font-family:"Montserrat",Arial,sans-serif;font-weight:900;font-size:30px;color:var(--red);letter-spacing:1px}
.brand-dot{width:26px;height:26px;border-radius:50%;background:var(--red)}
.header-right{display:flex;flex-direction:column;align-items:flex-end;gap:14px}
.header-top{display:flex;align-items:center;gap:18px}
.call{display:flex;align-items:center;gap:8px}
.call-icon{width:28px;height:28px;border-radius:50%;background:var(--red);display:flex;align-items:center;justify-content:center}
.call small{display:block;font-size:9px;color:var(--muted);line-height:1.1;font-weight:600}
.call strong{font-family:"Montserrat",Arial,sans-serif;font-size:16px;color:var(--red);line-height:1.1}
.nav{display:flex;align-items:center;gap:22px;font-size:11px;font-weight:700;color:var(--ink)}
.nav .home{width:30px;height:30px;border-bottom:3px solid var(--red);display:flex;align-items:flex-start;justify-content:center}

/* hero */
.hero{height:500px;background:linear-gradient(180deg,var(--night2) 0%,var(--night1) 55%,var(--night3) 100%);position:relative;overflow:hidden}
.hero-scene{position:absolute;inset:0}
.hero-copy{position:absolute;left:230px;top:60px;color:var(--white)}
.hero-copy h1{font-size:58px;font-weight:900;line-height:1;letter-spacing:1px}
.hero-copy p{font-family:"Montserrat",Arial,sans-serif;font-size:24px;font-weight:800;line-height:1.15;margin-top:8px;text-transform:uppercase}
.hero-cams{position:absolute;left:260px;top:230px;width:340px;height:230px;border-radius:8px;background:radial-gradient(ellipse at center,#f4f5f7 0%,#c9ccd3 60%,rgba(201,204,211,0) 72%)}
.quote{position:absolute;left:650px;top:18px;width:310px;height:460px;background:var(--red);padding:22px 22px}
.quote h2{color:var(--white);font-size:20px;font-weight:800;text-align:center;letter-spacing:.5px;margin-bottom:14px}
.field{height:30px;background:var(--white);margin-bottom:10px;font-size:11px;color:var(--muted);padding:6px 10px}
.field-row{display:flex;gap:10px}
.field-row .field{flex:1}
.field.area{height:84px}
.quote p{color:var(--white);font-size:10px;line-height:1.5;margin:4px 0 14px}
.quote .btn{display:block;text-align:center;padding:12px 0}

/* about */
.about{height:600px;padding-top:90px}
.about-body{display:flex;gap:30px;margin-top:60px}
.about-media{width:340px;height:300px;display:grid;grid-template-columns:2fr 1fr;grid-template-rows:1fr 1fr;gap:8px}
.about-media .ph:first-child{grid-row:1/3;background:linear-gradient(160deg,#d9e2ea,#8fa3b3)}
.about-media .ph:nth-child(2){background:linear-gradient(160deg,#c7cfd6,#6d7b88)}
.about-media .ph:nth-child(3){background:linear-gradient(160deg,#b9c2ca,#55616c)}
.about-text{flex:1;font-size:11.5px}
.about-text p{margin-bottom:12px}
.about-text .lead{color:var(--ink);font-weight:700}

/* services */
.services{height:640px;background:var(--red);padding-top:70px}
.service-grid{display:grid;grid-template-columns:repeat(3,1fr);gap:30px 28px;margin-top:50px}
.service .ph{height:150px;border:3px solid var(--white)}
.service h3{color:var(--white);font-size:13px;font-weight:700;margin-top:10px;line-height:1.3}
.s1{background:linear-gradient(150deg,#d3d6db,#7e858e)}
.s2{background:linear-gradient(150deg,#b8c1c9,#4f5b66)}
.s3{background:linear-gradient(150deg,#9fb28a,#6b5845)}
.s4{background:linear-gradient(150deg,#5b4d44,#1e1a18)}
.s5{background:linear-gradient(150deg,#e0e1e3,#8d9096)}
.s6{background:linear-gradient(150deg,#9db4c8,#3e5062)}

/* products */
.products{height:640px;padding-top:70px}
.product-grid{position:relative;height:420px;margin-top:50px}
.product{position:absolute;width:210px;height:190px;background:var(--light);padding:12px;text-align:center}
.product h4{font-family:"Open Sans",Arial,sans-serif;font-size:10px;font-weight:600;color:var(--ink)}
.product .ph{width:130px;height:110px;margin:10px auto 8px;background:radial-gradient(circle,#d8d9dc,#f3f3f4 70%)}
.product small{font-size:9px;color:var(--muted)}
.p1{left:0;top:0}.p2{left:550px;top:0}.p3{left:0;top:230px}.p4{left:550px;top:230px}
.p5{left:260px;top:110px;width:240px}
.products .more{text-align:center;margin-top:-10px}

/* automation */
.automation{height:580px;background:var(--light);padding-top:70px}
.automation .section-title{font-size:22px;line-height:1.3;text-align:center}
.automation .section-title span{display:block}
.auto-art{position:relative;width:560px;height:330px;margin:40px auto 0}
.auto-house{position:absolute;left:30px;top:0;width:460px;height:270px;background:linear-gradient(180deg,#e9ecf0,#c5ccd4)}
.auto-phone{position:absolute;right:20px;top:10px;width:110px;height:220px;border-radius:14px;background:linear-gradient(180deg,#2a2c31,#121316)}
.auto-band{position:absolute;left:0;right:0;bottom:0;height:52px;background:var(--orange);border-radius:0 0 30px 30px;display:flex;align-items:center;justify-content:center;gap:8px;color:var(--white);font-family:"Montserrat",Arial,sans-serif;font-size:12px;font-weight:600}
.auto-band strong{font-size:18px;font-weight:600}

/* news */
.news{height:470px;padding-top:70px}
.news-grid{display:grid;grid-template-columns:repeat(3,1fr);gap:28px;margin-top:50px}
.news-card .ph{height:140px}
.n1{background:linear-gradient(150deg,#cfd5db,#6f7a85)}
.n2{background:linear-gradient(150deg,#dfe3e6,#8a949c)}
.n3{background:linear-gradient(150deg,#e3dcd2,#8f7f6e)}
.news-card time{display:block;font-size:9px;color:var(--muted);margin-top:10px}
.news-card h3{font-size:10.5px;font-weight:800;color:var(--ink);line-height:1.3;margin:4px 0 6px;padding-left:8px;border-left:3px solid var(--red)}
.news-card p{font-size:9.5px;line-height:1.5}

/* skyline */
.skyline{height:90px;background:linear-gradient(180deg,var(--white) 0%,var(--white) 20%,var(--red) 20%,var(--red-dark) 100%)}

/* footer */
.site-footer{height:340px;background:var(--footer);color:#b9bcc1;padding-top:50px;font-size:10.5px}
.footer-cols{display:grid;grid-template-columns:1.4fr 1fr 1.1fr 1.3fr;gap:26px}
.site-footer h4{color:var(--white);font-size:11px;font-weight:700;margin-bottom:14px;text-transform:uppercase}
.site-footer li{list-style:none;margin-bottom:7px;display:flex;gap:8px;align-items:flex-start}
.site-footer li svg{flex:none;margin-top:3px}
.socials{display:flex;gap:8px;margin-bottom:14px}
.socials span{width:24px;height:24px;border-radius:50%;border:1px solid #6c6f74}
.copyright{border-top:1px solid #2a2b2e;margin-top:40px;padding-top:18px;text-align:center;font-size:10px;color:#80848a}
</style>
</head>
<body>

<header class="site-header">
  <div class="wrap">
    <div class="brand"><span class="brand-dot"></span>NORTHGATE</div>
    <div class="header-right">
      <div class="header-top">
        <div class="call">
          <span class="call-icon"><svg width="14" height="14" viewBox="0 0 24 24"><path fill="#fff" d="M6.6 10.8a15.1 15.1 0 0 0 6.6 6.6l2.2-2.2c.3-.3.7-.4 1-.2 1.1.4 2.3.6 3.6.6.6 0 1 .4 1 1V20c0 .6-.4 1-1 1A17 17 0 0 1 3 4c0-.6.4-1 1-1h3.5c.6 0 1 .4 1 1 0 1.3.2 2.5.6 3.6.1.3 0 .7-.2 1z"/></svg></span>
          <div><small>CALL US</small><strong>713-555-0142</strong></div>
        </div>
        <span class="btn">Get a Free Quote</span>
      </div>
      <nav class="nav">
        <span class="home"><svg width="16" height="16" viewBox="0 0 24 24"><path fill="#e4202a" d="M12 3 2 12h3v8h5v-6h4v6h5v-8h3z"/></svg></span>
        <span>ABOUT US</span><span>SERVICES ▾</span><span>PRODUCTS</span><span>BLOG</span><span>CONTACT US</span>
      </nav>
    </div>
  </div>
</header>

<section class="hero">
  <div class="hero-scene ph" role="img" aria-label="City skyline at night with lit towers reflected in water"></div>
  <div class="hero-copy">
    <h1>NORTHGATE</h1>
    <p>A great place for your<br>security needs</p>
  </div>
  <div class="hero-cams ph" role="img" aria-label="Two white wireless security cameras"></div>
  <form class="quote">
    <h2>GET A FREE QUOTE</h2>
    <div class="field">Name</div>
    <div class="field">Email</div>
    <div class="field-row"><div class="field">Phone</div><div class="field">Zip</div></div>
    <div class="field area">Message</div>
    <p>By clicking the button below you agree that Northgate Signal Shield may contact you by phone, text or email about your free quote. We never share your details and you can opt out at any time. Licensed and insured with over 25 years of experience.</p>
    <span class="btn btn-dark">Get a Free Quote</span>
  </form>
</section>

<section class="about">
  <div class="wrap">
    <h2 class="section-title">About Us</h2>
    <div class="about-body">
      <div class="about-media">
        <div class="ph" role="img" aria-label="Technician at a security monitoring desk with headset"></div>
        <div class="ph" role="img" aria-label="Alarm keypad mounted on a wall"></div>
        <div class="ph" role="img" aria-label="Outdoor security camera on a building"></div>
      </div>
      <div class="about-text">
        <p class="lead">Northgate Signal Shield has protected homes and businesses for over 25 years. We are licensed and insured, and we offer security at competitive prices.</p>
        <p>From alarm monitoring to security cameras, access control and gate openers, our team designs each system around the way you live and work. Every install is handled by trained local technicians.</p>
        <p>We also install home theater systems, covert cameras and fire alarms with monitoring. Call us Monday to Friday, 8am to 5pm, and we will visit your property for a free quote with no pressure.</p>
        <span class="btn">Learn More</span>
      </div>
    </div>
  </div>
</section>

<section class="services">
  <div class="wrap">
    <h2 class="section-title light">Our Services</h2>
    <div class="service-grid">
      <div class="service"><div class="ph s1" role="img" aria-label="Ceiling security cameras"></div><h3>Security Cameras</h3></div>
      <div class="service"><div class="ph s2" role="img" aria-label="Card reader access control at a door"></div><h3>Access Control</h3></div>
      <div class="service"><div class="ph s3" role="img" aria-label="Automatic driveway gate"></div><h3>Gate Openers</h3></div>
      <div class="service"><div class="ph s4" role="img" aria-label="Home theater room with large screen"></div><h3>Home Theater Systems</h3></div>
      <div class="service"><div class="ph s5" role="img" aria-label="Small hidden covert camera"></div><h3>Covert Camera<br>Installations</h3></div>
      <div class="service"><div class="ph s6" role="img" aria-label="Technician at a fire alarm monitoring station"></div><h3>Fire Alarm Installation<br>and Monitoring</h3></div>
    </div>
  </div>
</section>

<section class="products">
  <div class="wrap">
    <h2 class="section-title">Products</h2>
    <div class="product-grid">
      <div class="product p1"><h4>Wireless Alarm Panel (1)</h4><div class="ph" role="img" aria-label="Wireless alarm control panel"></div><small>Read More ›</small></div>
      <div class="product p2"><h4>Dome Camera (2)</h4><div class="ph" role="img" aria-label="Black dome security camera"></div><small>Read More ›</small></div>
      <div class="product p5"><h4>Network Video Recorder (NVR) (3)</h4><div class="ph" role="img" aria-label="Network video recorder with four cameras"></div><small>Read More ›</small></div>
      <div class="product p3"><h4>HD Security Camera (4)</h4><div class="ph" role="img" aria-label="White bullet security camera"></div><small>Read More ›</small></div>
      <div class="product p4"><h4>Digital Video Recorder (DVR) (5)</h4><div class="ph" role="img" aria-label="Digital video recorder box"></div><small>Read More ›</small></div>
    </div>
    <div class="more"><span class="btn">View All</span></div>
  </div>
</section>

<section class="automation">
  <div class="wrap">
    <h2 class="section-title"><span>Home Automation and Security<br>System Service</span></h2>
    <div class="auto-art">
      <div class="auto-house ph" role="img" aria-label="Cutaway house with smart security devices in each room"></div>
      <div class="auto-phone ph" role="img" aria-label="Smartphone showing the security control app"></div>
      <div class="auto-band">powered by <strong>Homelinq</strong></div>
    </div>
  </div>
</section>

<section class="news">
  <div class="wrap">
    <h2 class="section-title">Latest News</h2>
    <div class="news-grid">
      <article class="news-card"><div class="ph n1" role="img" aria-label="Technician fitting a ceiling camera"></div><time>05 JUN 2019</time><h3>HOW TO CHOOSE THE RIGHT CAMERA FOR YOUR HOME</h3><p>Resolution, night vision and storage all matter. Here is what to weigh before you buy a new system.</p></article>
      <article class="news-card"><div class="ph n2" role="img" aria-label="Wall mounted camera outside a building"></div><time>05 JUN 2019</time><h3>WHY MONITORED ALARMS KEEP BUSINESSES SAFER</h3><p>A monitored alarm sends help fast, even when nobody is on site. Learn how our team responds.</p></article>
      <article class="news-card"><div class="ph n3" role="img" aria-label="Installer adjusting a camera on a porch"></div><time>05 JUN 2019</time><h3>FIVE SIMPLE STEPS TO SECURE YOUR PROPERTY</h3><p>Lighting, locks and cameras work best together. Start with these easy checks around your home.</p></article>
    </div>
  </div>
</section>

<div class="skyline ph" role="img" aria-label="Red city skyline silhouette"></div>

<footer class="site-footer">
  <div class="wrap">
    <div class="footer-cols">
      <div>
        <h4>Contact Info</h4>
        <ul>
          <li><svg width="10" height="10" viewBox="0 0 24 24"><path fill="#e4202a" d="M6.6 10.8a15.1 15.1 0 0 0 6.6 6.6l2.2-2.2c.3-.3.7-.4 1-.2 1.1.4 2.3.6 3.6.6.6 0 1 .4 1 1V20c0 .6-.4 1-1 1A17 17 0 0 1 3 4c0-.6.4-1 1-1h3.5c.6 0 1 .4 1 1 0 1.3.2 2.5.6 3.6.1.3 0 .7-.2 1z"/></svg>713-555-0142</li>
          <li><svg width="10" height="10" viewBox="0 0 24 24"><path fill="#e4202a" d="M2 5h20v14H2zm2 2v.5l8 5 8-5V7z"/></svg>Northgatess@ferntopmail.com</li>
          <li><svg width="10" height="10" viewBox="0 0 24 24"><path fill="#e4202a" d="M12 2a7 7 0 0 0-7 7c0 5 7 13 7 13s7-8 7-13a7 7 0 0 0-7-7zm0 9.5A2.5 2.5 0 1 1 12 6.5a2.5 2.5 0 0 1 0 5z"/></svg>P.O. Box 419 Crosby, TX 77064</li>
          <li><svg width="10" height="10" viewBox="0 0 24 24"><circle cx="12" cy="12" r="10" fill="#e4202a"/></svg>Mon–Fri 8am–5pm</li>
        </ul>
      </div>
      <div>
        <h4>Quick Links</h4>
        <ul><li>About Us</li><li>Gallery</li><li>Blog</li><li>Contact Us</li></ul>
      </div>
      <div>
        <h4>Services</h4>
        <ul><li>Alarm Monitoring</li><li>Security Cameras</li><li>Access Control</li><li>Gate Openers</li></ul>
      </div>
      <div>
        <h4>Follow Us</h4>
        <div class="socials"><span></span><span></span><span></span><span></span></div>
        <ul><li>Company license #K52948316</li><li>Fire license# TMV-6614027</li><li>JLP-8170326</li></ul>
      </div>
    </div>
    <div class="copyright">Copyright © 2019 Northgate Signal Shield LLC. All rights reserved.</div>
  </div>
</footer>

</body>
</html>
```